Dental Business Card

We are looking for a double sided business card that can be easily customized with the names of the different members of our dental team.

I would like the background to be the 2-tone blue fleur-de-lis type pattern on the sides of our website (www.harborlanegrins.com).

I would like the logo attached incorporated.

I would like our address (4872 Pell Orchard Drive, Suite 100, Williamsburg, VA 23412), phone number (757-318-4590), fax number (757-318-2764), website (www.harborlanegrins.com), and email address (info@harborlanegrins.com) all included on the front side.

Something a little more artistic to complement/highlight the logo on the back would be interesting.

I would like the business card to look professional, slightly feminine, and expense.

Reason: Still looking for the perfect design.

```html
<!DOCTYPE html>
<html lang="en">
<head>
<meta charset="utf-8">
<title>Harbor Lane Grins – Business Card</title>
<link rel="stylesheet" href="https://fonts.googleapis.com/css2?family=Exo+2:wght@400;500&family=Saira+Condensed:wght@600&display=swap">
<style>
  :root {
    --stage: #1d1e21;
    --paper: #ffffff;
    --paper-shade: #eceef1;
    --blue: #1a5cab;
    --blue-deep: #144d92;
    --blue-bright: #2a8fe0;
    --ink-white: #ffffff;
  }
  * { box-sizing: border-box; margin: 0; padding: 0; }
  html, body { width: 1200px; height: 863px; overflow: hidden; }
  body {
    background: var(--stage);
    position: relative;
    font-family: "Exo 2", sans-serif;
  }
  .card {
    position: absolute;
    width: 600px;
    height: 343px;
    overflow: hidden;
    box-shadow: 0 14px 30px rgba(0,0,0,.55);
  }

  /* Back side */
  .card--back { left: 120px; top: 80px; background: var(--blue); }
  .card--back .panel {
    position: absolute;
    left: 118px; top: 92px;
    width: 400px; height: 150px;
    background: linear-gradient(180deg, var(--paper) 0%, var(--paper-shade) 100%);
    display: flex; align-items: center; justify-content: center;
  }
  .card--back .website {
    position: absolute;
    right: 92px; top: 262px;
    color: var(--ink-white);
    font-size: 13px;
    letter-spacing: .3px;
  }

  /* Wordmark */
  .wordmark {
    display: flex; align-items: center; gap: 10px;
    color: var(--blue);
    font-size: 22px;
    font-weight: 500;
    letter-spacing: .5px;
  }
  .wordmark .dot {
    width: 14px; height: 14px; border-radius: 50%;
    background: var(--blue);
  }

  /* Front side */
  .card--front {
    left: 480px; top: 440px;
    background: linear-gradient(160deg, var(--paper) 0%, var(--paper-shade) 100%);
  }
  .card--front .shapes { position: absolute; inset: 0; }
  .card--front .brand {
    position: absolute;
    left: 0; top: 0; width: 270px; height: 343px;
    display: flex; align-items: center; justify-content: center;
  }
  .card--front .wordmark { font-size: 19px; }
  .person {
    position: absolute;
    left: 305px; top: 72px;
    color: var(--ink-white);
  }
  .person .name {
    font-family: "Saira Condensed", sans-serif;
    font-weight: 600;
    font-size: 34px;
    line-height: 1;
    text-transform: uppercase;
    letter-spacing: .5px;
  }
  .person .role {
    font-size: 11px;
    letter-spacing: 1px;
    text-transform: uppercase;
    margin-top: 4px;
  }
  .contact {
    position: absolute;
    left: 380px;
    color: var(--ink-white);
    font-size: 12.5px;
    line-height: 1.35;
  }
  .contact--address { top: 170px; }
  .contact--phone { top: 222px; }
  .contact--online { top: 273px; }
</style>
</head>
<body>

  <section class="card card--back" aria-label="Business card, back">
    <div class="panel">
      <div class="wordmark"><span class="dot"></span>Harbor Lane Grins</div>
    </div>
    <p class="website">www.harborlanegrins.com</p>
  </section>

  <section class="card card--front" aria-label="Business card, front">
    <svg class="shapes" width="600" height="343" viewBox="0 0 600 343">
      <polygon points="285,0 600,0 600,343 285,343" fill="var(--blue)"/>
      <polygon points="285,0 600,0 600,52 285,52" fill="var(--blue-deep)"/>
      <polygon points="250,60 600,60 600,148 300,148 275,125 250,125" fill="var(--blue-bright)"/>
      <polygon points="300,148 362,148 362,343 300,343" fill="var(--blue-deep)"/>

      <!-- pin -->
      <circle cx="331" cy="189" r="16" fill="var(--paper)"/>
      <path d="M331 180 a6 6 0 0 1 6 6 c0 5 -6 11 -6 11 s-6 -6 -6 -11 a6 6 0 0 1 6 -6z" fill="var(--blue)"/>
      <circle cx="331" cy="186" r="2.2" fill="var(--paper)"/>

      <!-- phone -->
      <circle cx="331" cy="240" r="16" fill="var(--paper)"/>
      <path d="M323 237 q8 -7 16 0 l-2 3 h-3 l-1 -2 q-4 -1 -4 0 l-1 2 h-3 z" fill="var(--blue)"/>
      <rect x="324" y="241" width="14" height="7" rx="1.5" fill="var(--blue)"/>
      <circle cx="331" cy="244.5" r="2" fill="var(--paper)"/>

      <!-- globe -->
      <circle cx="331" cy="291" r="16" fill="var(--paper)"/>
      <g fill="none" stroke="var(--blue)" stroke-width="1.6">
        <circle cx="331" cy="291" r="8.5"/>
        <ellipse cx="331" cy="291" rx="3.8" ry="8.5"/>
        <line x1="322.5" y1="291" x2="339.5" y2="291"/>
        <line x1="324" y1="286" x2="338" y2="286"/>
        <line x1="324" y1="296" x2="338" y2="296"/>
      </g>
    </svg>

    <div class="brand">
      <div class="wordmark"><span class="dot"></span>Harbor Lane Grins</div>
    </div>

    <div class="person">
      <p class="name">Clara Whitfield</p>
      <p class="role">General Manager</p>
    </div>

    <p class="contact contact--address">4872 Pell Orchard Drive,<br>Suite 100, Williamsburg</p>
    <p class="contact contact--phone">757-318-4590<br>757-318-2764</p>
    <p class="contact contact--online">info@harborlanegrins.com<br>www.harborlanegrins.com</p>
  </section>

</body>
</html>
```